Need a flyer to email blast investors, realtors and property owners offering my realty & property management services of the following....

I'm a Danfield Morrow agent offering an all service Real Estate & Property Management services to assist with buying, selling, renting & managing properties for owner of single family residence, multi family units, investment properties, HOA, seasonal equine rentals, vacation rentals and absentee owners.

Tenant Portal: Pay rent online, online application, tenant background criminal & eviction screening, search properties, sign lease online, view rent history and submit repairs and maintenance orders.

Owner Portal: Easy payment, financial statements, maintenance report and owners monthly and annual report.

Maintenance Portal: Conduct annual and move out inspections, create and generate work orders, easy communication with vendors and property managers, post photos directly into website for owner and tenant viewing.

Concierge service: for absentee owners we assist and offer groceries, personal shopping, car service & maintenance, property vendor access, maid service. seasonal rentals and airport pickup.

Offer an agent referral fee and 1st month property management fee FREE.

My company info..
Tolver Realty & Property Management
www,tolverrealtypm.example
555-318-4096

Target Market(s)

Realtors, investors, property owners, condos, investors and HOA

Industry/Entity Type

Property Management

Font styles to use
Decorative

Colors
86cfc6
33b8a4

Requirements
Must have
• I'm a Danfield Morrow agent offering an all service Real Estate & Property Management services to assist with buying, selling, renting & managing properties for owner of single family residence, multi family units, investment properties, HOA, seasonal equine rentals, vacation rentals and absentee owners.
• Tenant Portal: Pay rent online, online application, tenant background criminal & eviction screening, search properties, sign lease online, view rent history and submit repairs and maintenance orders.
• Owner Portal: Easy payment, financial statements, maintenance report and owners monthly and annual report.
• Maintenance Portal: Conduct annual and move out inspections, create and generate work orders, easy communication with vendors and property managers, post photos directly into website for owner and tenant viewing.
• Concierge service: for absentee owners we assist and offer groceries, personal shopping, car service & maintenance, property vendor access, maid service. seasonal rentals and airport pickup.
• Offer an agent referral fee and 1st month property management fee FREE.
• My company info..
• Tolver Realty & Property Management
• www,tolverrealtypm.example
• 555-318-4096
Nice to have
• pictures of happy people, houses, beaches, multi units.
Should not have
• n/a

```html
<!DOCTYPE html>
<html lang="en">
<head>
<meta charset="utf-8">
<title>Tolver Realty &amp; Property Management Flyer</title>
<link rel="stylesheet" href="https://fonts.googleapis.com/css2?family=Playfair+Display:wght@700&family=Cinzel:wght@600&family=Oswald:wght@500;700&family=Open+Sans:wght@400;700&display=swap">
<style>
  :root {
    --teal-light: #86cfc6;
    --teal: #33b8a4;
    --teal-dark: #1f6f66;
    --teal-deep: #175a53;
    --ink: #3c3c3c;
    --paper: #ffffff;
  }
  * { margin: 0; padding: 0; box-sizing: border-box; }
  html, body { width: 889px; height: 1200px; overflow: hidden; background: var(--paper); }
  .flyer { position: relative; width: 889px; height: 1200px; background: var(--paper); font-family: "Open Sans", sans-serif; color: var(--ink); overflow: hidden; }
  .deco { position: absolute; left: 0; top: 0; }
  .interior-photo { position: absolute; left: 0; top: 130px; width: 889px; height: 500px; background: linear-gradient(160deg, #dfe9ec 0%, #c6d6d8 40%, #e9e4dc 75%, #cfc5b8 100%); clip-path: polygon(0 8%, 100% 0, 100% 88%, 60% 100%, 0 92%); }
  .title { position: absolute; right: 28px; top: 28px; text-align: center; width: 460px; }
  .title-main { font-family: "Playfair Display", serif; font-size: 40px; color: var(--teal-dark); line-height: 1.1; }
  .title-sub { font-family: "Cinzel", serif; font-size: 31px; color: var(--teal-dark); letter-spacing: 1px; margin-top: 4px; border-top: 2px solid var(--teal); padding-top: 4px; }
  .offer-badge { position: absolute; left: 95px; top: 440px; width: 240px; text-align: center; color: #fff; font-family: "Oswald", sans-serif; }
  .offer-badge .tag { background: var(--teal-deep); padding: 8px 6px; font-size: 28px; font-weight: 700; box-shadow: 0 3px 6px rgba(0,0,0,.3); }
  .offer-badge .term { background: var(--teal); padding: 6px; font-size: 22px; font-weight: 500; line-height: 1.2; }
  .offer-badge .free { background: var(--teal-deep); font-size: 52px; font-weight: 700; padding: 2px 0 6px; }
  .intro { position: absolute; left: 36px; top: 665px; width: 470px; font-size: 14px; line-height: 1.5; }
  .intro strong { color: #222; }
  .portal { position: absolute; left: 36px; width: 470px; display: flex; align-items: center; gap: 14px; }
  .portal-label { flex: 0 0 138px; height: 46px; background: var(--teal); color: #fff; font-weight: 700; font-size: 14px; display: flex; align-items: center; padding-left: 10px; clip-path: polygon(0 0, 88% 0, 100% 50%, 88% 100%, 0 100%); }
  .portal-text { font-size: 13px; line-height: 1.45; border-bottom: 1px solid var(--teal-light); padding-bottom: 6px; }
  .concierge { position: absolute; left: 520px; top: 640px; width: 340px; }
  .concierge h2 { background: var(--teal-deep); color: #fff; font-family: "Oswald", sans-serif; font-weight: 500; font-size: 24px; padding: 8px 14px; letter-spacing: .5px; }
  .concierge p { background: var(--teal); color: #fff; font-size: 19px; line-height: 1.45; padding: 16px 20px; text-align: center; }
  .agent-photo { position: absolute; left: 660px; top: 975px; width: 229px; height: 225px; background: radial-gradient(ellipse at 50% 40%, #c9a58d 0%, #6b4a3a 55%, #e8e3df 100%); }
  .contact { position: absolute; left: 300px; top: 1098px; width: 350px; color: #fff; font-size: 16px; line-height: 1.6; font-weight: 700; white-space: nowrap; }
  .contact .row { display: flex; align-items: center; gap: 8px; }
  .contact svg { flex: 0 0 16px; }
  .brand { position: absolute; left: 36px; top: 1112px; display: flex; align-items: center; gap: 8px; font-family: "Open Sans", sans-serif; font-weight: 700; font-size: 18px; color: var(--teal-deep); }
  .brand .mark { width: 18px; height: 18px; background: var(--teal-deep); }
</style>
</head>
<body>
<div class="flyer">
  <div class="interior-photo" role="img" aria-label="Bright modern condo living room with white sofas and ocean-view windows"></div>

  <svg class="deco" width="889" height="1200" viewBox="0 0 889 1200" aria-hidden="true">
    <path d="M0 0 H380 C300 40 160 90 0 150 Z" fill="var(--teal)"/>
    <path d="M0 0 H260 C190 40 90 80 0 110 Z" fill="var(--teal-dark)"/>
    <path d="M0 585 C260 640 560 630 889 540 V600 C560 690 260 700 0 650 Z" fill="var(--teal-light)"/>
    <path d="M0 610 C260 660 560 650 889 570 V590 C560 680 260 690 0 640 Z" fill="var(--teal)"/>
    <path d="M0 1070 C200 1050 420 1080 660 1070 L660 1200 H0 Z" fill="var(--teal)"/>
    <path d="M0 1165 C250 1130 600 1190 889 1150 V1200 H0 Z" fill="var(--teal-dark)"/>
    <rect x="0" y="1088" width="660" height="4" fill="var(--teal-light)"/>
  </svg>

  <header class="title">
    <div class="title-main">Tolver Realty &amp; Property</div>
    <div class="title-sub">MANAGEMENT SERVICES</div>
  </header>

  <div class="offer-badge">
    <div class="tag">Agent Referral fee</div>
    <div class="term">1st Month<br>Property Management fee</div>
    <div class="free">FREE</div>
  </div>

  <section class="concierge">
    <h2>CONCIERGE SERVICE:</h2>
    <p>For absentee owners we assist and offer groceries, personal shopping, car service &amp; maintenance, property vendor access, maid service, seasonal rentals and airport pickup.</p>
  </section>

  <p class="intro">I'm a Danfield Morrow agent offering an all service Real Estate &amp; Property Management services to assist with <strong>buying, selling, renting &amp; managing properties</strong> for owner of single family residence, multi family units, investment properties, HOA, seasonal equine rentals, vacation rentals and absentee owners.</p>

  <div class="portal" style="top:815px">
    <div class="portal-label">TENANT PORTAL:</div>
    <div class="portal-text">Pay rent online, online application, tenant background criminal &amp; eviction screening, search properties, sign lease online, view rent history and submit repairs and maintenance orders.</div>
  </div>
  <div class="portal" style="top:905px">
    <div class="portal-label">OWNER PORTAL:</div>
    <div class="portal-text">Easy payment, financial statements, maintenance report and owners monthly and annual report.</div>
  </div>
  <div class="portal" style="top:975px">
    <div class="portal-label">MAINTENANCE PORTAL:</div>
    <div class="portal-text">Conduct annual and move out inspections, create and generate work orders, easy communication with vendors and property managers, post photos directly into website for owner and tenant viewing.</div>
  </div>

  <div class="brand"><span class="mark"></span>Danfield Morrow</div>

  <div class="contact">
    <div class="row">Tolver Realty &amp; Property Management</div>
    <div class="row"><svg width="16" height="16" viewBox="0 0 16 16"><circle cx="8" cy="8" r="7" fill="none" stroke="#fff" stroke-width="1.6"/><path d="M1 8h14M8 1c-3 4-3 10 0 14M8 1c3 4 3 10 0 14" fill="none" stroke="#fff" stroke-width="1.2"/></svg>www,tolverrealtypm.example</div>
    <div class="row"><svg width="16" height="16" viewBox="0 0 16 16"><path d="M3 1l3 3-2 2c1 2 3 4 5 5l2-2 3 3-2 3C7 15 1 9 0 3z" fill="#fff"/></svg>555-318-4096</div>
  </div>

  <div class="agent-photo" role="img" aria-label="Portrait of the smiling real estate agent"></div>
</div>
</body>
</html>
```